A Lantern Over Quiet Waters: Words of renewal Dr. Wendell O. Pike, Sr.

Redesign on a book cover jacket. Previous cover attached.

Target Market(s)

Women 30-70

Industry/Entity Type

Religious

Requirements
Must have
• a heart of some sort on cover.
Nice to have
• This needs to appeal to someone who is struggling with life and having difficult times. A damaged or broken heart should be on the cover. . Very upscale.
Should not have
• No animations

```html
<!DOCTYPE html>
<html lang="en">
<head>
<meta charset="utf-8">
<title>A Lantern Over Quiet Waters — Book Jacket</title>
<link rel="stylesheet" href="https://fonts.googleapis.com/css2?family=EB+Garamond:ital,wght@0,400;0,500;1,600;1,700&family=Barlow:wght@500&display=swap">
<style>
  :root {
    --jacket-red: #cc1b1f;
    --title-red: #8a1c1c;
    --paper: #ffffff;
    --ink: #1c1c1c;
    --crackle-light: #f4f2ef;
    --crackle-shade: #d9d5d0;
    --heart-bright: #e4452e;
    --heart-deep: #c02a1c;
  }
  * { margin: 0; padding: 0; box-sizing: border-box; }
  html, body { width: 1200px; height: 838px; overflow: hidden; background: var(--paper); }
  .jacket { position: relative; width: 1200px; height: 838px; background: var(--paper); font-family: "EB Garamond", serif; }

  /* Back cover */
  .back-cover { position: absolute; left: 0; top: 0; width: 555px; height: 838px; background: var(--paper); }
  .back-band { position: absolute; left: 0; top: 126px; width: 555px; height: 68px; background: var(--jacket-red);
    color: var(--paper); font-size: 28px; letter-spacing: 1.5px; text-align: center; line-height: 68px; text-transform: uppercase; }
  .back-blurb { position: absolute; left: 96px; top: 236px; width: 372px; font-size: 15.4px; line-height: 18.1px;
    color: var(--ink); text-align: center; white-space: nowrap; }
  .code-box { position: absolute; left: 364px; top: 696px; width: 150px; height: 83px; border: 1px solid var(--ink); background: var(--paper); }

  /* Spine */
  .spine { position: absolute; left: 555px; top: 0; width: 91px; height: 838px; background: var(--jacket-red); color: var(--paper); }
  .spine-title, .spine-author { position: absolute; left: 45px; writing-mode: vertical-rl; white-space: nowrap; transform: translateX(-50%); }
  .spine-title { top: 50px; font-size: 28.5px; letter-spacing: 1px; text-transform: uppercase; }
  .spine-author { top: 596px; font-size: 20px; font-style: italic; font-weight: 600; }

  /* Front cover */
  .front-cover { position: absolute; left: 646px; top: 0; width: 554px; height: 838px; overflow: hidden;
    background: radial-gradient(ellipse at 50% 50%, var(--crackle-light) 0%, #ebe8e4 70%, var(--crackle-shade) 100%); }
  .front-title { position: absolute; left: 0; top: 44px; width: 554px; text-align: center; color: var(--title-red); text-transform: uppercase; line-height: 1; }
  .front-title .title-lead { display: block; font-size: 43px; font-weight: 500; letter-spacing: 0.5px; }
  .front-title .title-main { display: block; font-size: 96px; font-weight: 500; margin-top: 2px; line-height: 82px; }
  .heart-art { position: absolute; left: 74px; top: 268px; width: 392px; height: 388px;
    background: radial-gradient(ellipse 50% 50% at 50% 48%, var(--heart-bright) 0%, var(--heart-deep) 62%, rgba(192,42,28,0) 100%); }
  .subtitle { position: absolute; left: 0; top: 660px; width: 554px; text-align: center; font-style: italic; font-weight: 600;
    font-size: 29px; line-height: 36px; color: var(--ink); }
  .foreword { position: absolute; left: 0; top: 768px; width: 554px; text-align: center; font-family: "Barlow", sans-serif;
    font-weight: 500; font-size: 19px; letter-spacing: 0.4px; color: var(--ink); text-transform: uppercase; }
</style>
</head>
<body>
<main class="jacket">
  <section class="back-cover">
    <div class="back-band">A Lantern Over Quiet Waters</div>
    <p class="back-blurb">Cernam, apidige ndeles res magnam santi blabore pere-<br>henis utasperum inihil magnat accaborpos sus.<br>Neque volorep eribus. Sed endem simporit facepellab<br>intiossit, ut fugiatusci ipsant, solorruptat ipsum del ipiet<br>ommoluptatem quidio. Nem volume pliatur rernam<br>alit, eseditatem eos sum dis essinusdae volupta erenis-<br>ciae coratur, qui voluptae etur, eaquo venis non niscient<br>re escienet entem re milis non niminvel ipsaest explit<br>andaerumet aut vendella exeri nonse porro que explam,<br>archicab iur? Umque que et latur rem rernatur alicati as-<br>perfe rrovidel id excessimi, ilita cuptiatem adi iusci occati<br>aciis dolores veritibus et ut etur sit doloribea corionse<br>dolupta si vidicipsa dis voluptatem alitae porumqui con<br>cusam alibusa nissitem eostint quodis eum fugitissinus<br>aut doluptae nonsed que nullore rferum re, omnimo<br>voluptatia cumquam facium explabo risquatum reperum<br>eatempo rroraest atur a aspitio quat asimus, od quati<br>consedit vendit raeceri aeraescia doluptae nullandignam<br>evenem as aliaspis ipsamenimil moluptatem invelent offic<br>torio et de nullorepuda consequas que cus nienet qui aut<br>et hari remosam aliquis</p>
    <div class="code-box"></div>
  </section>

  <section class="spine">
    <div class="spine-title">A Lantern Over Quiet Waters</div>
    <div class="spine-author">Dr. Wendell O. Pike, Sr.</div>
  </section>

  <section class="front-cover" role="img" aria-label="Cracked dry white earth texture covering the front cover">
    <h1 class="front-title">
      <span class="title-lead">A Lantern Over</span>
      <span class="title-main">Quiet</span>
      <span class="title-main">Waters</span>
    </h1>
    <div class="heart-art" role="img" aria-label="Photograph of a red leaf-textured heart broken apart by deep cracks in dry earth"></div>
    <p class="subtitle">Words of renewal<br>by Dr. Wendell O. Pike, Sr.</p>
    <p class="foreword">Foreword by Dr. Marcus T. Holloway, Jr</p>
  </section>
</main>
</body>
</html>
```